Price list for young Botox clinic

I require a price list/Treatment menu for clinic

To include:
Logo
Address
Phone number
Website

List of services and Prices
Botox 1 area £100
Botox 2 areas £150
Botox 3 areas £200
Lip Enhancement 0.5ml £100
Lip Enhancement 1ml £200
Facial Fillers £200 per 1ml
Vivorel £450 per session (2 vials - must be bought as a course)
Non Surgical Face Lift (Thread Lift) £600 per area
Derma Stamp Full Face £250
Derma Stamp Small Per Small Area £100
Cryo Therapy £60
Chemical Peel Light Peel and Microdermabrasion £85
Chemical Peel Deep Peel £150
Consultation £30 redeemable against service
Botox Top Up Botox £50 (must be within 2 weeks of 1st treatment)
Filler Top Up £100 (must be within 2 weeks of 1st appointment)

Open Hours
Updates

Company Name: MBH Address: 52 Fenwick Lane, 4 Marlow Parade, KT9 3QD Phone: 0208 947 2186 Website: www.mirabellhoughaesthetics.co.uk

Please add more colour

Needs to be much cleaner and simpler Front page to include logo and price list Back page to inculde open hours and contact information including google map. Please no images with needles. Images of lips and faces are good, but try not to crowd copy on the pagei. No copy on top of images. White, grey, black and reds are good on colouring.

Target Market(s)

young market ages 22-45 years old mainly female
modern

Industry/Entity Type

Clinic

Number of Pages Required

4 page

Requirements
Must have
• Logo - logo must be in colour grey/silver
• Address (small map?)
• Phone number
• Web address
• Services
• Open hours
• Prices
• Images

```html
<!DOCTYPE html>
<html lang="en">
<head>
<meta charset="utf-8">
<title>MBH Aesthetics – Opening Times &amp; Location</title>
<link href="https://fonts.googleapis.com/css2?family=Italianno&family=Questrial&family=Libre+Baskerville&display=swap" rel="stylesheet">
<style>
  :root {
    --page-light: #ffffff;
    --page-edge: #d6d6d6;
    --frame: #9c9c9c;
    --ink: #4a4a4a;
    --ink-soft: #5a5a5a;
    --panel-top: #ffffff;
    --panel-mid: #dcdcdc;
    --oval: #9a9a9a;
    --map-light: #ebe8e1;
    --map-dark: #e0dbd1;
    --map-border: #a8a8a8;
  }
  * { box-sizing: border-box; margin: 0; padding: 0; }
  html, body { width: 852px; height: 1200px; overflow: hidden; }
  body {
    position: relative;
    background: radial-gradient(ellipse at 50% 45%, var(--page-light) 35%, var(--page-edge) 100%);
    color: var(--ink);
  }
  .page-frame {
    position: absolute; left: 20px; top: 12px; width: 814px; height: 1170px;
    border: 3px solid var(--frame);
  }
  .hours-card { position: absolute; left: 0; top: 0; width: 852px; height: 400px; }
  .hours-title {
    position: absolute; left: 278px; top: 82px; width: 304px; text-align: center;
    font-family: "Italianno", cursive; font-weight: 400; font-size: 50px; color: #fff; line-height: 1;
  }
  .hours-list {
    position: absolute; left: 163px; top: 170px; width: 560px;
    font-family: "Questrial", sans-serif; font-size: 25px; color: var(--ink-soft);
    letter-spacing: 1.9px; line-height: 27.5px; list-style: none;
  }
  .hours-list li { display: flex; }
  .hours-list .day { width: 192px; }
  .hours-list .dots { width: 120px; letter-spacing: 2.5px; }
  .hours-list .time { flex: 1; text-align: center; }
  .contact {
    position: absolute; left: 0; top: 402px; width: 852px; text-align: center;
    font-family: "Libre Baskerville", serif; color: var(--ink);
  }
  .contact-heading {
    font-family: "Italianno", cursive; font-weight: 400; font-size: 72px; line-height: 74px;
    color: var(--ink);
  }
  .contact-address { font-size: 30px; line-height: 42px; }
  .contact-phone { font-size: 31px; line-height: 42px; }
  .contact-email, .contact-web { font-size: 24px; line-height: 35px; }
  .location-map {
    position: absolute; left: 50px; top: 651px; width: 746px; height: 413px;
    border: 3px solid var(--map-border); border-radius: 12px;
    background: linear-gradient(135deg, var(--map-light), var(--map-dark));
  }
  .tagline {
    position: absolute; left: 0; top: 1080px; width: 852px; text-align: center;
    font-family: "Italianno", cursive; font-size: 76px; color: var(--ink); line-height: 1;
  }
</style>
</head>
<body>
  <div class="page-frame"></div>

  <svg class="hours-card" viewBox="0 0 852 400" aria-hidden="true">
    <defs>
      <linearGradient id="panelSheen" x1="0" y1="0" x2="0" y2="1">
        <stop offset="0" stop-color="#ffffff"/>
        <stop offset="0.5" stop-color="#dcdcdc"/>
        <stop offset="1" stop-color="#ffffff"/>
      </linearGradient>
      <filter id="panelShadow" x="-5%" y="-10%" width="110%" height="125%">
        <feDropShadow dx="0" dy="3" stdDeviation="4" flood-color="#000" flood-opacity="0.25"/>
      </filter>
    </defs>
    <g filter="url(#panelShadow)">
      <ellipse cx="430" cy="112" rx="172" ry="57" fill="#fff"/>
      <rect x="87" y="110" width="673" height="275" rx="10" fill="url(#panelSheen)"/>
    </g>
    <ellipse cx="430" cy="112" rx="152" ry="40" fill="#9a9a9a" stroke="#fff" stroke-width="3"/>
  </svg>
  <h1 class="hours-title">Opening Times</h1>

  <ul class="hours-list">
    <li><span class="day">Monday</span><span class="dots">.........</span><span class="time">10am-4pm</span></li>
    <li><span class="day">Tuesday</span><span class="dots">.........</span><span class="time">10am-4pm</span></li>
    <li><span class="day">Wednesday</span><span class="dots">.........</span><span class="time">12pm-8pm</span></li>
    <li><span class="day">Thursday</span><span class="dots">.........</span><span class="time">7:30am-4:30pm</span></li>
    <li><span class="day">Friday</span><span class="dots">.........</span><span class="time">10am-2pm</span></li>
    <li><span class="day">Saturday</span><span class="dots">.........</span><span class="time">9am-2pm</span></li>
    <li><span class="day">Sunday</span><span class="dots">.........</span><span class="time">Closed</span></li>
  </ul>

  <section class="contact">
    <h2 class="contact-heading">We are at:</h2>
    <p class="contact-address">4 Marlow Parade, Surrey, KT9 3QD</p>
    <p class="contact-phone">Phone: 020 8947 2186</p>
    <p class="contact-email">Email: mbhmarlowbookings@mailbox.co.uk</p>
    <p class="contact-web">www.mirabellhoughaesthetics.co.uk</p>
  </section>

  <div class="location-map" role="img" aria-label="Street map showing the clinic location on Marlow Parade"></div>

  <p class="tagline">Achieve a fresh and beautiful you.</p>
</body>
</html>
```